Chewable Dog Supplements jar with lid

Below are some specifications of this project: 
There will be 6 different types of dog supplements in different jars, which will have different colors, or elements(dogs),  but will respect the same theme overall.  I attached some pictures below as a reference.
 The design I would like to create is for a label that will go around and on the top of a round plastic jar. The size of the product label is 25cm long and 8.5 cm high and on the top there is a circle that goes on the lid with the exact same design as on the front.
Some small pictures on the back with no Grain, Corn or Soy derivates  
 All products come in different shapes chews 
All products have 3 different headlines with their benefits that go on the front of the design.
All products have different flavors.
Regarding the text that will go on the back of the product, I can help with adding that to all products as long as we agree on how it looks. On the back I will need a space for a barcode, best before date, there should be 2 tables with ingredients and directions for use, and space for text under :Storage instructions, Warning, Description.

Target Market(s)

Europe

Industry/Entity Type

pet food

Requirements
Must have
• Trust signals ( Free from GMO, Natural ingredients, Free from artificial colouring) and a text box with the benefits of the product that I will provide.

```html
<!DOCTYPE html>
<html lang="en">
<head>
<meta charset="utf-8">
<title>Chewable Dog Supplements – Jar Labels</title>
<link href="https://fonts.googleapis.com/css2?family=Montserrat:wght@300;700&family=Roboto+Condensed:wght@400;700&display=swap" rel="stylesheet">
<style>
  :root{
    --stage:#9a9a9a;
    --label-black:#141414;
    --ink:#1a1a1a;
    --white:#ffffff;
    --calm:#b18fe0;
    --calm-band:#ad8bdc;
    --vita:#aeea1f;
    --vita-band:#a9e61c;
    --chew-tone:#d8cf9a;
    --chew-dark:#8a6a3c;
  }
  *{box-sizing:border-box;margin:0;padding:0}
  html,body{width:1200px;height:1200px;overflow:hidden}
  body{background:var(--stage);position:relative;font-family:"Roboto Condensed",sans-serif}

  .label{position:absolute;top:553px;width:500px;height:354px;background:var(--label-black);overflow:hidden}
  .label--calming{left:60px;--accent:var(--calm);--band:var(--calm-band)}
  .label--multivitamin{left:640px;--accent:var(--vita);--band:var(--vita-band)}

  .title-swatch{position:absolute;left:38px;top:20px;width:270px;height:126px}
  .title{position:absolute;left:42px;top:52px;width:262px;text-align:center;color:var(--ink);font-family:"Montserrat",sans-serif}
  .title__main{display:block;font-weight:700;font-size:38px;line-height:40px;letter-spacing:-0.5px}
  .label--multivitamin .title__main{font-size:28px;letter-spacing:-0.3px;margin-top:8px;line-height:32px}
  .title__sub{display:block;font-weight:300;font-size:27px;line-height:30px;letter-spacing:9px;padding-left:9px}

  .brand{position:absolute;left:368px;top:34px;width:64px;display:flex;flex-direction:column;align-items:center;gap:8px;color:var(--white)}
  .brand__dot{width:26px;height:26px;border:1.5px solid var(--white);border-radius:50%}
  .brand__name{font-family:"Montserrat",sans-serif;font-weight:300;font-size:9px;line-height:11px;letter-spacing:2.5px;padding-left:2.5px}

  .benefits{position:absolute;left:51px;top:157px;list-style:none;color:var(--white);font-size:15px;line-height:23px}
  .label--multivitamin .benefits{top:151px}
  .benefits li{display:flex;align-items:center;gap:4px}
  .benefits svg{width:14px;height:8px;fill:var(--accent)}

  .trust{position:absolute;left:60px;top:242px;display:flex;gap:12px}
  .trust__badge{width:30px;height:30px;border:1.5px solid #d9d9d9;border-radius:50%}

  .band{position:absolute;left:0;bottom:0;width:100%;height:68px;background:var(--band)}

  .dog-photo{position:absolute;bottom:0;border-radius:60px 60px 0 0}
  .label--calming .dog-photo{left:318px;top:92px;width:138px;background:linear-gradient(180deg,#5a2e1a 0%,#6b3820 40%,#e8e2dc 70%,#5a2e1a 100%)}
  .label--multivitamin .dog-photo{left:306px;top:98px;width:156px;background:linear-gradient(180deg,#3d3d40 0%,#2f2f33 60%,#262629 100%)}

  .chews-photo{position:absolute;left:202px;top:250px;width:104px;height:64px;border-radius:30px;background:radial-gradient(ellipse at 50% 45%,var(--chew-tone) 0%,#c9bd85 55%,var(--chew-dark) 100%)}
  .label--multivitamin .chews-photo{left:196px}

  .flavor{position:absolute;left:75px;top:300px;width:86px;height:30px;display:flex;border:1.5px solid var(--white)}
  .flavor__icon{width:30px;display:flex;align-items:center;justify-content:center;background:var(--white)}
  .flavor__icon span{width:16px;height:12px;border:1.5px solid var(--band);border-radius:50%}
  .flavor__text{flex:1;display:flex;align-items:center;justify-content:center;text-align:center;font-weight:700;font-size:10px;line-height:10px;color:var(--white);background:var(--band)}
  .label--multivitamin .flavor{border-color:var(--ink);background:var(--ink)}
  .label--multivitamin .flavor__icon{background:var(--ink);border-right:1.5px solid var(--white)}
  .label--multivitamin .flavor__icon span{border-color:var(--white)}
  .label--multivitamin .flavor__text{background:var(--ink);color:var(--vita)}

  .audience{position:absolute;left:84px;top:333px;font-size:9.5px;color:var(--white)}
  .label--multivitamin .audience{color:var(--ink)}

  .count{position:absolute;left:222px;top:330px;width:66px;text-align:center;color:var(--white)}
  .label--multivitamin .count{left:218px;color:var(--ink)}
  .count__main{display:block;font-weight:700;font-size:13px;line-height:13px}
  .count__weight{display:block;font-size:5.5px;line-height:7px;white-space:nowrap}
</style>
</head>
<body>

<section class="label label--calming">
  <svg class="title-swatch" viewBox="0 0 270 126" aria-hidden="true"><path fill="var(--accent)" d="M22 24 L120 16 L180 6 L236 26 L252 58 L270 72 L240 96 L214 108 L120 112 L60 120 L16 104 L0 70 L10 44 Z"/></svg>
  <h1 class="title"><span class="title__main">CALMING</span><span class="title__sub">CHEWS</span></h1>
  <div class="brand"><span class="brand__dot"></span><span class="brand__name">PAWVERA</span></div>
  <ul class="benefits">
    <li><svg viewBox="0 0 14 8"><rect x="2" y="2" width="10" height="4"/><circle cx="2" cy="2" r="2"/><circle cx="2" cy="6" r="2"/><circle cx="12" cy="2" r="2"/><circle cx="12" cy="6" r="2"/></svg>Helps manage normal stress</li>
    <li><svg viewBox="0 0 14 8"><rect x="2" y="2" width="10" height="4"/><circle cx="2" cy="2" r="2"/><circle cx="2" cy="6" r="2"/><circle cx="12" cy="2" r="2"/><circle cx="12" cy="6" r="2"/></svg>Promotes relaxation</li>
    <li><svg viewBox="0 0 14 8"><rect x="2" y="2" width="10" height="4"/><circle cx="2" cy="2" r="2"/><circle cx="2" cy="6" r="2"/><circle cx="12" cy="2" r="2"/><circle cx="12" cy="6" r="2"/></svg>Helps restless dogs</li>
  </ul>
  <div class="trust"><span class="trust__badge"></span><span class="trust__badge"></span><span class="trust__badge"></span></div>
  <div class="band"></div>
  <div class="dog-photo" role="img" aria-label="Photo of a brown and white sheepdog sitting"></div>
  <div class="chews-photo" role="img" aria-label="Photo of three round filled dog chews"></div>
  <div class="flavor"><span class="flavor__icon"><span></span></span><span class="flavor__text">BEEF<br>LAVOR</span></div>
  <p class="audience">Supoport For Dog</p>
  <p class="count"><span class="count__main">60 CHEWS</span><span class="count__weight">NET WT 5.29 oz (150g)</span></p>
</section>

<section class="label label--multivitamin">
  <svg class="title-swatch" viewBox="0 0 270 126" aria-hidden="true"><path fill="var(--accent)" d="M22 24 L120 16 L180 6 L236 26 L252 58 L270 72 L240 96 L214 108 L120 112 L60 120 L16 104 L0 70 L10 44 Z"/></svg>
  <h1 class="title"><span class="title__main">MULTIVITAMIN</span><span class="title__sub">CHEWS</span></h1>
  <div class="brand"><span class="brand__dot"></span><span class="brand__name">PAWVERA</span></div>
  <ul class="benefits">
    <li><svg viewBox="0 0 14 8"><rect x="2" y="2" width="10" height="4"/><circle cx="2" cy="2" r="2"/><circle cx="2" cy="6" r="2"/><circle cx="12" cy="2" r="2"/><circle cx="12" cy="6" r="2"/></svg>Strong inmunity</li>
    <li><svg viewBox="0 0 14 8"><rect x="2" y="2" width="10" height="4"/><circle cx="2" cy="2" r="2"/><circle cx="2" cy="6" r="2"/><circle cx="12" cy="2" r="2"/><circle cx="12" cy="6" r="2"/></svg>Hip and joint support</li>
    <li><svg viewBox="0 0 14 8"><rect x="2" y="2" width="10" height="4"/><circle cx="2" cy="2" r="2"/><circle cx="2" cy="6" r="2"/><circle cx="12" cy="2" r="2"/><circle cx="12" cy="6" r="2"/></svg>Skin and coat health</li>
  </ul>
  <div class="trust"><span class="trust__badge"></span><span class="trust__badge"></span><span class="trust__badge"></span></div>
  <div class="band"></div>
  <div class="dog-photo" role="img" aria-label="Photo of a dark grey puppy looking at the viewer"></div>
  <div class="chews-photo" role="img" aria-label="Photo of three round filled dog chews"></div>
  <div class="flavor"><span class="flavor__icon"><span></span></span><span class="flavor__text">SALMON<br>FLAVOR</span></div>
  <p class="audience">Supoport For Dog</p>
  <p class="count"><span class="count__main">60 CHEWS</span><span class="count__weight">NET WT 5.29 oz (150g)</span></p>
</section>

</body>
</html>
```